Fun relaxed Travel Photography Business Card*

Require a fun, funky and quirky but rememberable business card for a travel photographer

Industry/Entity Type

Photographer

Contact Information for Business Card

Front Card

(my name) Tavo M.

Travel Photographer ( small under travel photographer) “self-proclaimed”

(website logo) wanderingtavo.example

(Instagram logo) @wandering_with_tavo

(Instagram logo) @wandering_with_tavo_2.0 (backup for when Instagram puts Tavo on timeout for bad behaviour)

Tel: N/A (removing the potential awkwardness of me not replying)

Email: (see above)

Back Card

Offending people since 1986

(Bottom right corner) “p.s. travelling made me fatTER”

Font styles to use
Serif

Colors

Designer to choose colors to be used in the design.

Requirements
Must have
• a camera
• a similar cartoon version of me as the "logo" see attached files, try to make as similar as possible

```html
<!DOCTYPE html>
<html lang="en">
<head>
<meta charset="utf-8">
<title>Tavo M. — Travel Photographer Business Card</title>
<link rel="stylesheet" href="https://fonts.googleapis.com/css2?family=Open+Sans:wght@400;700&display=swap">
<style>
  :root{
    --stage:#e9e9ea;
    --card-dark:#2b2b2c;
    --card-light:#f6f6f6;
    --red:#dd1c24;
    --ink:#1d1d1d;
    --white:#ffffff;
    --chair:#f0b52e;
    --chair-deep:#d99a1c;
  }
  html,body{margin:0;padding:0;overflow:hidden;}
  body{
    width:1200px;height:1021px;background:var(--stage);
    font-family:"Open Sans",Arial,sans-serif;position:relative;
  }
  .card{position:absolute;width:640px;height:380px;}
  .card-shape{position:absolute;inset:0;filter:drop-shadow(0 10px 18px rgba(0,0,0,.22));}
  .card--back{left:500px;top:70px;}
  .card--front{left:70px;top:540px;}

  /* back side */
  .avatar-ring{position:absolute;left:86px;top:78px;width:232px;height:232px;border-radius:50%;
    border:4px solid var(--red);box-sizing:border-box;display:flex;align-items:center;justify-content:center;}
  .avatar{width:206px;height:206px;border-radius:50%;
    background:radial-gradient(circle at 50% 40%,#e42a2f 0%,#c8151c 100%);}
  .tagline{position:absolute;left:360px;top:172px;width:250px;margin:0;text-align:center;
    color:var(--red);font-weight:700;font-size:25px;line-height:1.05;}
  .postscript{position:absolute;right:34px;top:288px;margin:0;color:var(--white);
    font-size:20px;font-weight:400;}

  /* front side */
  .name{position:absolute;left:48px;top:88px;margin:0;color:var(--red);font-weight:700;
    font-size:32px;letter-spacing:1px;text-transform:uppercase;line-height:1;}
  .role{position:absolute;left:48px;top:128px;margin:0;color:var(--ink);font-size:20px;line-height:1.05;}
  .contacts{position:absolute;left:48px;top:214px;margin:0;padding:0;list-style:none;
    color:var(--ink);font-size:22px;line-height:1.2;}
  .contacts li{display:flex;align-items:center;gap:6px;}
  .contacts svg{flex:none;}
  .mark{width:14px;height:14px;border:2px solid var(--red);border-radius:3px;box-sizing:border-box;flex:none;}
  .lounge{position:absolute;right:36px;bottom:26px;width:230px;height:130px;border-radius:14px;
    background:linear-gradient(135deg,var(--chair) 0%,var(--chair-deep) 100%);}
</style>
</head>
<body>

<section class="card card--back" aria-label="Back of card">
  <svg class="card-shape" width="640" height="380" viewBox="0 0 640 380" aria-hidden="true">
    <path fill="var(--card-dark)" d="M24 50 H60 V30 Q60 14 76 14 H150 V20 Q150 0 170 0 H430 Q450 0 450 20 V38 H600 Q614 38 614 50 H616 Q640 50 640 74 V356 Q640 380 616 380 H24 Q0 380 0 356 V74 Q0 50 24 50 Z"/>
  </svg>
  <div class="avatar-ring"><div class="avatar" role="img" aria-label="Cartoon portrait of Tavo in sunglasses and a floral shirt on a red circle"></div></div>
  <p class="tagline">Offending people since 1986</p>
  <p class="postscript">“p.s. travelling made me fatTER”</p>
</section>

<section class="card card--front" aria-label="Front of card">
  <svg class="card-shape" width="640" height="380" viewBox="0 0 640 380" aria-hidden="true">
    <path fill="var(--card-light)" d="M24 50 H40 V20 Q40 0 60 0 H160 Q180 0 180 20 V50 H340 V20 Q340 0 360 0 H580 Q600 0 600 20 V50 H616 Q640 50 640 74 V356 Q640 380 616 380 H24 Q0 380 0 356 V74 Q0 50 24 50 Z"/>
  </svg>
  <h1 class="name">Tavo M.</h1>
  <p class="role">Travel Photographer<br>“self-proclaimed”</p>
  <ul class="contacts">
    <li>
      <svg width="16" height="16" viewBox="0 0 16 16" aria-hidden="true">
        <g fill="none" stroke="var(--red)" stroke-width="1.6">
          <circle cx="8" cy="8" r="6.6"/><ellipse cx="8" cy="8" rx="3" ry="6.6"/><path d="M1.4 8 H14.6"/>
        </g>
      </svg>wanderingtavo.example
    </li>
    <li><span class="mark" aria-hidden="true"></span>@wandering_with_tavo</li>
    <li><span class="mark" aria-hidden="true"></span>@wandering_with_tavo_2.0</li>
  </ul>
  <div class="lounge" role="img" aria-label="Cartoon of Tavo lounging in a yellow armchair beside a small table with a drink"></div>
</section>

</body>
</html>
```